Biz card for my counselling/social work practice

Biz card design for my counselling practice, focus on well-being, I am a social worker who also teaches meditation and workshops but my main focus for the card is my counselling practice. My website reveals a gentle flowing quality which I would life reflected in my card. This business card will be designed to share with other practitioners who are looking for support with their clients to take their healing to another level or well-being.

Target Market(s)

professionals seeking mental health counselling/men/women/ those seeking to improve their well-being through insight based counselling to optimize their lives and process trauma or limiting patterns

Industry/Entity Type

Counsellor

Contact Information for Business Card

Info on the card: perhaps text is aligned left?
Maribel Strand, MSW, RSW
Counsellor
614.295.3140
info@maribelstrand.example
www.maribelstrand.example

Please use a modern font doesn’t need to be the one chosen below. Thank you

Font styles to use
Serif

Colors
3176b5
33a6d7
33b8a4
6b449b
abd037
d2a4cc
e55fa2

Requirements
Must have
• My business card details on front
• Backside
• Accelerated Resolution Therapy
• Cognitive Behavioral Therapy
• Mindfulness Informed Therapy
Nice to have
• I would like the card to be basic, (white or creme without too much bold colour) and with perhaps a stripe or band of vertical colour in blue or green (or a merge of colour) perhaps embossed or in a negative space. (this is one idea, but do not want the card to be too feminine or interest only women as i see men too so this is only an idea, but not 100 percent on this.
• I do not have a logo. I would prefer to heart from my website not to be used in the design as i am considering modifying this and re-branding.
Should not have
• too bold colours or bright yellow/blacks. i Like tones that are greens, blues.

```html
<!DOCTYPE html>
<html lang="en">
<head>
<meta charset="utf-8">
<title>Maribel Strand — Business Card</title>
<link rel="stylesheet" href="https://fonts.googleapis.com/css2?family=Oswald:wght@400&family=Montserrat:wght@300&display=swap">
<style>
  :root {
    --backdrop: #e9ecef;
    --card: #fafafa;
    --brand-blue: #3a67a8;
    --band-start: #4574ae;
    --band-end: #6b95c7;
    --band-text: #ffffff;
    --contact-text: #4a6fa3;
    --icon-green: #8fbf3c;
  }
  * { margin: 0; padding: 0; box-sizing: border-box; }
  html, body {
    width: 1200px;
    height: 936px;
    overflow: hidden;
    background: var(--backdrop);
  }
  .card {
    position: absolute;
    left: 100px;
    top: 160px;
    width: 1000px;
    height: 616px;
    background: var(--card);
    box-shadow: 0 6px 24px rgba(0, 0, 0, 0.12);
  }
  .brand {
    position: absolute;
    left: 60px;
    top: 86px;
    display: flex;
    align-items: center;
    gap: 28px;
  }
  .brand-dot {
    width: 120px;
    height: 120px;
    border-radius: 50%;
    background: var(--icon-green);
    flex: none;
  }
  .brand-name {
    font-family: "Oswald", sans-serif;
    font-weight: 400;
    font-size: 74px;
    line-height: 1;
    color: var(--brand-blue);
    letter-spacing: 0.5px;
    text-transform: uppercase;
  }
  .band {
    position: absolute;
    left: 0;
    top: 252px;
    width: 100%;
    height: 118px;
    background: linear-gradient(90deg, var(--band-start), var(--band-end));
    padding: 26px 0 0 228px;
    color: var(--band-text);
  }
  .holder {
    font-family: "Oswald", sans-serif;
    font-weight: 400;
    font-size: 38px;
    line-height: 1;
    text-transform: uppercase;
  }
  .holder .divider { margin: 0 8px; }
  .holder .credentials { font-size: 30px; }
  .role {
    font-family: "Montserrat", sans-serif;
    font-weight: 300;
    font-size: 27px;
    margin-top: 6px;
  }
  .contacts {
    position: absolute;
    left: 228px;
    top: 438px;
    list-style: none;
  }
  .contact {
    display: flex;
    align-items: center;
    gap: 14px;
    height: 36px;
    font-family: "Montserrat", sans-serif;
    font-weight: 300;
    font-size: 27px;
    color: var(--contact-text);
    letter-spacing: 0.5px;
  }
  .contact svg { width: 26px; height: 26px; flex: none; }
</style>
</head>
<body>
  <main class="card">
    <header class="brand">
      <span class="brand-dot"></span>
      <span class="brand-name">Maribel Strand</span>
    </header>

    <section class="band">
      <p class="holder">Maribel Strand<span class="divider">|</span><span class="credentials">MSW, RSW</span></p>
      <p class="role">Counsellor</p>
    </section>

    <ul class="contacts">
      <li class="contact">
        <svg viewBox="0 0 26 26" aria-hidden="true" fill="none" stroke="var(--icon-green)" stroke-width="1.8">
          <circle cx="13" cy="13" r="11"/>
          <path d="M9 8 L11 8 L12 11 L10.5 12 Q12 15 14 15.5 L15 14 L18 15 L18 17 Q15 19 11.5 16 Q8 13 9 8 Z"/>
        </svg>
        <span>614.295.3140</span>
      </li>
      <li class="contact">
        <svg viewBox="0 0 26 26" aria-hidden="true" fill="none" stroke="var(--icon-green)" stroke-width="1.8">
          <rect x="2" y="6" width="22" height="15"/>
          <path d="M2 6 L13 15 L24 6"/>
        </svg>
        <span>info@maribelstrand.example</span>
      </li>
      <li class="contact">
        <svg viewBox="0 0 26 26" aria-hidden="true" fill="none" stroke="var(--icon-green)" stroke-width="1.8">
          <circle cx="13" cy="13" r="11"/>
          <ellipse cx="13" cy="13" rx="5" ry="11"/>
          <path d="M2 13 H24 M4 8 H22 M4 18 H22"/>
        </svg>
        <span>www.maribelstrand.example</span>
      </li>
    </ul>
  </main>
</body>
</html>
```